The Driftwood Caster----- Wade Pellman----- Kellow Creek Bronzeback ------www.thedriftwoodcaster.test-----

Hello Fishermen,
The Umpqua rivers peaceful beauty is like no other river, the private Hollis section offers trophy bass fishing along with 100 fish days. Spin cast or fly fish for bass. This 8 hour fishing trip takes you into a remote section of ranches and wilderness abundant with not only thousands of bass per mile...... but wildlife and scenery are breath taking in this quite section of river.
This trip is for everyone, easy for the Grand Parents and the grand kids...... Women love this trip with the warm weather and easy fishing.
So Let's go Fishing...... please call or email us today and book your trip or with any questions you have.
Vacation Rentals, Motels and R.V parks all available close by.

Email us at: driftwoodcaster@mailbrook.test
Visit our website at: www.thedriftwoodcaster.test
Call us at: 541-555-0148

Thank you for fishing with us,
Wade Pellman

return address;
Wade Pellman
p.o. box 712
Elkton, Oregon 97521

****NOTE for front of post card layout person should go to our website home page for ideas, and photos. Please feel free to change our message above to correct grammar and make read smoother, Thank you.....

there is no contest....not sure how that got there...

```html
<!DOCTYPE html>
<html lang="en">
<head>
<meta charset="utf-8">
<title>The Driftwood Caster – Postcard</title>
<link rel="stylesheet" href="https://fonts.googleapis.com/css2?family=Source+Sans+3:wght@400;600;700&family=PT+Sans+Narrow:wght@700&family=Kalam&display=swap">
<style>
:root{
  --navy:#1b4e6d;
  --ink:#3a3a3a;
  --grey:#6d6e70;
  --grey-light:#d6d7d8;
  --page:#eeeeee;
  --card:#ffffff;
}
*{box-sizing:border-box;margin:0;padding:0}
html,body{width:1200px;height:770px;overflow:hidden}
body{background:var(--page);font-family:"Source Sans 3",sans-serif;color:var(--ink);position:relative}

.card{position:absolute;background:var(--card);overflow:hidden;box-shadow:0 4px 14px rgba(0,0,0,.18)}
.display{font-family:"PT Sans Narrow",sans-serif;font-weight:700;color:var(--navy)}

/* ---------- front ---------- */
.front{left:30px;top:40px;width:480px;height:620px}
.front .hero-photo{position:absolute;left:0;top:50px;width:480px;height:350px;
  background:linear-gradient(180deg,#4f7f86 0%,#6e9a9c 22%,#9fb3ad 40%,#5d7f7f 58%,#3d5e60 72%,#8a867a 86%,#b9b5ab 100%)}
.front .body-wash{position:absolute;left:0;top:380px;width:480px;height:200px;
  background:linear-gradient(180deg,#ffffff 0%,#f3f4f4 45%,#dfe1e2 100%)}
.front .header-shape,.front .mid-shape,.front .foot-shape{position:absolute;left:0;width:480px}
.front .header-shape{top:0;height:135px}
.front .mid-shape{top:290px;height:110px}
.front .foot-shape{bottom:0;height:80px}
.front .brand{position:absolute;top:11px;width:100%;text-align:center;font-size:33px;letter-spacing:.1px}
.front .owner{position:absolute;top:49px;width:100%;text-align:center;font-weight:700;font-size:17px;color:var(--navy)}
.front .tagline{position:absolute;left:285px;top:236px;font-family:"Kalam",cursive;font-size:21px;color:#fff;transform:rotate(-7deg);text-shadow:0 1px 2px rgba(0,0,0,.35)}
.front .inset-photo{position:absolute;left:20px;top:235px;width:112px;height:112px;border-radius:50%;border:4px solid #fff;
  background:linear-gradient(180deg,#b9cbd8 0%,#8fa3a8 30%,#6f8758 55%,#3e5c3a 100%);box-shadow:0 2px 6px rgba(0,0,0,.3)}
.front .trip-title{position:absolute;left:20px;top:368px;font-weight:700;font-size:16.5px;color:var(--navy)}
.front .trip-copy{position:absolute;left:20px;top:398px;width:385px;font-size:10.3px;line-height:1.38;color:#333}
.front .trip-copy p+p{margin-top:11px}
.front .cta{position:absolute;left:20px;top:504px;font-size:10.8px;font-weight:600;color:#222}
.front .contact-line{position:absolute;left:20px;top:521px;font-size:11.5px;font-weight:700;color:var(--navy)}
.front .web-label{position:absolute;left:28px;top:560px;font-size:11px;color:#fff}
.front .web-url{position:absolute;left:28px;top:575px;font-size:24px;font-weight:700;color:#fff;line-height:1.1}

/* ---------- back ---------- */
.back{left:545px;top:175px;width:620px;height:480px;background:linear-gradient(135deg,#fff 40%,#e4e5e8 100%)}
.back .mascot{position:absolute;left:14px;top:26px;width:112px;height:58px;border-radius:50% 40% 45% 50%;
  background:linear-gradient(135deg,#9aa86a,#5a6a33)}
.back .head-swoosh{position:absolute;left:60px;top:62px;width:320px;height:34px}
.back .brand{position:absolute;left:135px;top:18px;font-size:23px}
.back .owner{position:absolute;left:135px;top:46px;width:210px;text-align:center;font-weight:700;font-size:13px;color:var(--navy)}
.back .trip-title{position:absolute;left:135px;top:65px;width:210px;text-align:center;font-weight:700;font-size:13.5px;color:var(--navy)}
.back .return-address{position:absolute;left:384px;top:30px;font-size:9px;line-height:1.3;color:#111;font-style:normal}
.back .stamp-box{position:absolute;left:510px;top:25px;width:92px;height:62px;border:1.5px solid var(--grey-light)}
.back .address-lines{position:absolute;left:384px;top:176px;width:205px}
.back .address-lines span{display:block;height:1.5px;background:var(--grey-light);margin-bottom:26px}
.back .body{position:absolute;left:22px;top:135px;width:330px;font-size:10px;line-height:1.45;color:#333}
.back .body h3{font-size:11.5px;font-weight:700;color:var(--navy);margin:8px 0 4px}
.back .photo-frame{position:absolute;left:0;top:262px;width:220px;height:218px}
.back .family-photo{position:absolute;left:0;top:275px;width:195px;height:205px;border-top-right-radius:150px 205px;
  background:linear-gradient(180deg,#9fb6cc 0%,#7f9a8a 35%,#5c6e48 55%,#3a4a6a 80%,#2d3d58 100%)}
.back .thanks{position:absolute;left:150px;width:150px;top:292px;text-align:right;font-size:9px;font-weight:600;color:#333}
.back .thanks .sig{display:block;font-family:"Kalam",cursive;font-weight:400;font-size:9.5px;color:var(--grey);margin-top:2px}
.back .contact{position:absolute;left:234px;top:367px;font-style:normal}
.back .contact h4{font-size:10.5px;font-weight:700;color:var(--navy);line-height:1.2;margin-bottom:8px}
.back .contact li{list-style:none;display:flex;align-items:center;gap:8px;font-size:9px;color:#111;margin-bottom:5px}
.back .contact li.phone{font-size:11px}
.back .contact svg{width:11px;height:11px;flex:none}
</style>
</head>
<body>

<section class="card front">
  <div class="hero-photo" role="img" aria-label="Photo of a guide kneeling beside a drift boat on the river, holding two fish"></div>
  <div class="body-wash" role="img" aria-label="Faded photo of the drift boat behind the trip text"></div>
  <svg class="header-shape" viewBox="0 0 480 135" preserveAspectRatio="none">
    <defs><linearGradient id="hdrSwoosh" x1="0" x2="1"><stop offset="0" stop-color="#fff"/><stop offset=".55" stop-color="#a4a5a7"/><stop offset="1" stop-color="#3f4042"/></linearGradient></defs>
    <path d="M0 0H480V72C380 98 230 104 0 86Z" fill="#fff"/>
    <path d="M150 92C280 98 390 86 480 64V78C390 102 280 106 150 92Z" fill="url(#hdrSwoosh)"/>
  </svg>
  <div class="brand display">THE DRIFTWOOD CASTER</div>
  <div class="owner">Wade Pellman</div>
  <div class="tagline">Let's go Fishing!!!</div>
  <svg class="mid-shape" viewBox="0 0 480 110" preserveAspectRatio="none">
    <defs><linearGradient id="midSwoosh" x1="0" x2="1"><stop offset="0" stop-color="#c9cacb"/><stop offset=".5" stop-color="#858688"/><stop offset="1" stop-color="#5a5b5d"/></linearGradient></defs>
    <path d="M0 66C150 34 330 28 480 6V110H0Z" fill="url(#midSwoosh)"/>
    <path d="M0 82C160 54 330 50 480 40V110H0Z" fill="#fff"/>
  </svg>
  <div class="inset-photo" role="img" aria-label="Round photo of the river valley with forested hills"></div>
  <h2 class="trip-title">Kellow Creek Bronzeback</h2>
  <div class="trip-copy">
    <p>The Umpqua rivers peaceful beauty is like no other river, the private Hollis section offers trophy bass fishing along with 100 fish days. Spin cast or fly fish for bass.</p>
    <p>&nbsp;8 HOUR fishing trip takes you into a remote section of ranches and wilderness abundant with not only thousands of bass per mile...... but wildlife and scenery are breath taking in this quite section of river.</p>
  </div>
  <p class="cta">Please call or email us today and book your trip or with any questions you have.</p>
  <p class="contact-line">driftwoodcaster@mailbrook.test &nbsp;| www.thedriftwoodcaster.test | 541-555-0148</p>
  <svg class="foot-shape" viewBox="0 0 480 80" preserveAspectRatio="none">
    <path d="M0 12C180 0 360 2 480 16V80H0Z" fill="#bfc0c2"/>
    <path d="M0 18C180 6 360 8 480 22V80H0Z" fill="var(--navy)"/>
  </svg>
  <p class="web-label">Visit our website for more information</p>
  <p class="web-url">thedriftwoodcaster.test</p>
</section>

<section class="card back">
  <svg class="head-swoosh" viewBox="0 0 320 34" preserveAspectRatio="none">
    <defs><linearGradient id="backSwoosh" x1="0" x2="1"><stop offset="0" stop-color="#3f4042"/><stop offset=".6" stop-color="#a8a9ab"/><stop offset="1" stop-color="#fff"/></linearGradient></defs>
    <path d="M0 28C110 14 210 12 320 14C210 18 110 22 0 34Z" fill="url(#backSwoosh)"/>
  </svg>
  <div class="mascot" role="img" aria-label="Illustration of a leaping bass"></div>
  <div class="brand display">THE DRIFTWOOD CASTER</div>
  <div class="owner">Wade Pellman</div>
  <div class="trip-title">Kellow Creek Bronzeback</div>
  <address class="return-address">Wade Pellman<br>p.o. box 712<br>Elkton, Oregon 97521</address>
  <div class="stamp-box"></div>
  <div class="address-lines"><span></span><span></span><span></span><span></span><span></span></div>
  <div class="body">
    <p>This trip is for everyone, easy for the Grand Parents and the grand kids......<br>Women love this trip with the warm weather and easy fishing.</p>
    <h3>So Let's go Fishing......</h3>
    <p>Please call or email us today and book your trip or with any questions you have.<br>Vacation Rentals, Motels and R.V parks all available close by.</p>
  </div>
  <svg class="photo-frame" viewBox="0 0 220 218" preserveAspectRatio="none">
    <path d="M0 0C120 0 205 80 220 218H195C185 95 110 13 0 13Z" fill="#6d6e70"/>
  </svg>
  <div class="family-photo" role="img" aria-label="Photo of a father and son on the river holding a bass"></div>
  <p class="thanks">Thank you for fishing with us,<span class="sig">Wade Pellman</span></p>
  <address class="contact">
    <h4>Contact us or visit our website<br>for more information:</h4>
    <ul>
      <li class="phone"><svg viewBox="0 0 12 12"><circle cx="6" cy="6" r="5.4" fill="none" stroke="#333" stroke-width="1"/><path d="M4 3.2l1 1.2-.6.7c.4.9 1 1.5 1.9 1.9l.7-.6 1.2 1-.6 1C5.6 8.3 3.7 6.4 3.6 3.8Z" fill="#333"/></svg>541-555-0148</li>
      <li><svg viewBox="0 0 12 12"><rect x="1" y="3" width="10" height="6.5" rx="1" fill="#333"/><path d="M1.5 3.5L6 7l4.5-3.5" fill="none" stroke="#fff" stroke-width=".8"/></svg>driftwoodcaster@mailbrook.test</li>
      <li><svg viewBox="0 0 12 12"><circle cx="6" cy="6" r="5" fill="none" stroke="#333" stroke-width="1"/><ellipse cx="6" cy="6" rx="2.2" ry="5" fill="none" stroke="#333" stroke-width=".8"/><path d="M1 6h10" stroke="#333" stroke-width=".8"/></svg>www.thedriftwoodcaster.test</li>
    </ul>
  </address>
</section>

</body>
</html>
```